IT business looking for Standout Letterhead Design

We need a letterhead design for a company based in San Diego, CA called Corvane Systems, Inc. We specialize in IT engineering, installation and technical support pertaining to the department of defense.

We would like to see a design that incorporates the black and gold that matches our company logo.

More information on the company can be found at www.corvane-sys.example

```html
<!DOCTYPE html>
<html lang="en">
<head>
<meta charset="utf-8">
<title>Corvane Systems, Inc. — Letterhead</title>
<link rel="stylesheet" href="https://fonts.googleapis.com/css2?family=Ubuntu:wght@400;500;700&family=Yellowtail&display=swap">
<style>
  :root {
    --ink: #1d1d1b;
    --charcoal: #3a3a38;
    --gold: #ece22c;
    --gold-soft: #f3ec7a;
    --paper: #ffffff;
    --olive: #6f6d4a;
  }
  * { margin: 0; padding: 0; box-sizing: border-box; }
  html, body { width: 928px; height: 1200px; overflow: hidden; }
  body {
    font-family: "Ubuntu", Arial, sans-serif;
    color: var(--ink);
  }
  .letterhead {
    position: relative;
    width: 928px;
    height: 1200px;
    background: linear-gradient(90deg, var(--paper) 0%, var(--paper) 12%, #fdfbe6 38%, var(--gold-soft) 72%, var(--gold) 100%);
    overflow: hidden;
  }
  .corner-pattern { position: absolute; }
  .corner-pattern--top {
    left: 0; top: 0; width: 274px; height: 262px;
    background: linear-gradient(135deg, var(--ink) 0%, var(--charcoal) 45%, var(--gold) 100%);
    clip-path: polygon(0 0, 95% 0, 100% 45%, 70% 55%, 45% 75%, 20% 100%, 0 85%);
  }
  .corner-pattern--bottom {
    right: 0; bottom: 0; width: 278px; height: 252px;
    background: linear-gradient(315deg, var(--olive) 0%, #8c8a5a 45%, var(--gold) 100%);
    clip-path: polygon(60% 0, 80% 15%, 100% 10%, 100% 100%, 5% 100%, 0 72%, 25% 55%, 40% 30%);
  }
  .brand {
    position: absolute;
    left: 520px; top: 140px;
    width: 340px;
    display: flex; align-items: center; justify-content: center; gap: 12px;
  }
  .brand__mark { width: 22px; height: 22px; border-radius: 50%; background: var(--ink); flex: none; }
  .brand__name { font-weight: 700; font-size: 27px; color: var(--ink); letter-spacing: 0.5px; }
  .contact {
    position: absolute;
    left: 520px; top: 254px; width: 340px;
    text-align: center;
    font-size: 12px; line-height: 17px; font-weight: 500;
  }
  .contact__web { margin-top: 2px; }
  .recipient {
    position: absolute; left: 127px; top: 332px;
    font-size: 14px; line-height: 19px; font-weight: 500;
  }
  .letter {
    position: absolute; left: 127px; top: 412px; width: 614px;
    font-size: 14px; line-height: 19px; font-weight: 500;
  }
  .letter p { margin-bottom: 19px; text-align: justify; }
  .letter .salutation { margin-bottom: 10px; }
  .closing { margin-top: 8px; }
  .closing p { margin-bottom: 12px; }
  .signature {
    font-family: "Yellowtail", cursive;
    font-size: 32px; line-height: 38px; font-weight: 400;
  }
</style>
</head>
<body>
<main class="letterhead">
  <div class="corner-pattern corner-pattern--top" role="img" aria-label="Geometric pattern of black, charcoal and gold triangles"></div>
  <div class="corner-pattern corner-pattern--bottom" role="img" aria-label="Geometric pattern of olive, grey and gold triangles"></div>

  <header>
    <div class="brand">
      <span class="brand__mark"></span>
      <span class="brand__name">Corvane Systems, Inc.</span>
    </div>
    <address class="contact" style="font-style: normal;">
      <div>San Diego CA.</div>
      <div>619.555.0148</div>
      <div class="contact__web">www.corvane-sys.example &nbsp;info@corvane-sys.example</div>
    </address>
  </header>

  <section class="recipient">
    <div>To the General Director,</div>
    <div>Halvern Global Incorporated.</div>
    <div>20 / 07 /2014</div>
  </section>

  <article class="letter">
    <p class="salutation">Dear Sir / Madam</p>
    <p>Lorem ipsum dolor sit amet, consectetuer adipiscing elit. Nam cursus. Morbi ut mi. Li balam enim leo, egestas id, condimentum at, laoreet mattis, massa. Sed eleifend nos ummy diam. Praesent mauris ante, elementum et, bibendum at, posuere sit amet, nib duis tincidunt lectus quis dui viverra vestibulum. Suspendisse vulputate aliquam dui. Nulla elementum dui ut augue. Aliquam vehicula mi at mauris. Maecenas placerat sea si at consequat rhoncus, sem nunc gravida justo.</p>
    <p>Sed laoreet aliquamlii amet, consectetuer adipiscing elit. Nam cursus. Morbi ut mi. Lie balam enim leo, egestas id, condimentum at, laoreet mattis, massa. Sed eleifend nos ummy diam. Praesent mauris ante, elementum et, bibendum at.</p>
    <p>Nulla elementum dui ut augue. consectetuer adipiscing elit. Nam cursus. Morbi ut ma balam enim leo, egestas id, condimentum at, laoreet mattis, massa. Sed eleifend nos ummy diam. Praesent mauris ante, elementum et, bibendum at, posuere sit amet, nib duis tincidunt lectus quis dui viverra vestibulum. Suspendisse vulputate aliquam duifi. Nulla elementum dui ut augue. Aliquam vehicula mi at mauris. Maecenas placerat sef si at consequat rhoncus, sem nunc gravida justo.Fusce suscipit varius mi. Cum sociisz tes, nascetur ridiculus mus. Nulla dui. Morbi nunc odio, gravida at, cursus nec, luctusi lorem.Maecenas tristique orci ac sem. amin deso as. Duis ultricies pharetra agna. Dai nec accumsan malesuada orci. Donec</p>
    <p>liquam vehicula mi at mauris. Maecenas placerat se si at consequat rhoncus, sem nim gravida justo.Fusce suscipit varius mi. Cum sociis tes, nascetur ridiculus mus. Nulla al Morbi nunc odio, gravida at, cursus nec, luctusi. lorem.Maecenas tristique orci ac seai amin deso as.</p>
    <div class="closing">
      <p>Sincerely,</p>
      <p>Torben Asler.</p>
      <div class="signature">Torben</div>
    </div>
  </article>
</main>
</body>
</html>
```